Cd Cover Design needed for Electronic Music album

I need a cd cover design for my new album of Electronic music, sub-genre from Electronic to Techno to Tech-House to Dub-House.(just want people to Dance)
My artist name is "Velvet Circuitry" and the album is "Lantern of Drift". I have uploaded an image for artist name ,its just for the idea of how the letters go. Would like to see designs in blue was thinking of Audio equipment or audio wavs (looks like an earthquake meter) ,I am a fan of Masking images and puting another image inside, i would like the design to catch eyes and reach out for different and unique, my music ranges from soft to hard crunch within the same songs. I am excited to see what you come up with.
With many Thanks from Velvet Circuitry

I have uploaded 9 Design ideas,dont use the images i do not own them only downloaded, some of the images show the photoshop two image design.

the size and track names are below:

online distributor requires the size of 1448x1448
track font ,something straight and orderly (not to fancy for the lettering)
1. Meadow Vs Ironclad 6:54
2. Lantern of Drift 6:10
3. Z O Lively 8:04
4. Ever Roamin 7:04
5. Bound to wander 7:15
6. Fold into 5:40
7. Past the Lanterns gate 6:38

I would also like to have the designer(s) put on a small section on the inside cover designers contact info and type "designs by:" that way the designer gets some viewer coverage also.

Target Market(s)

Anyone that listens to Electronic / Techno / House / Dub.

Industry/Entity Type

Electronic

Colors
0455a3

Requirements
Must have
• The logo that I uploaded I was hoping that someone could design that better for me not using font style letters but drawn and put that together with the design. Please don't use my design that I uploaded (its not to appealing, its why im not a designer) ,its just to show how I want the letters. Also I like black as the background color.
Nice to have
• Image Masking ,like1, 2 or 3 images in one silhouette image, images done like from the album of Tinwharf except no squirrels ,Photoshop is a plus, really would like to see designs with real images that are masked with other images.

```html
<!DOCTYPE html>
<html lang="en">
<head>
<meta charset="utf-8">
<title>Lantern of Drift – CD Cover, Front and Back</title>
<link rel="stylesheet" href="https://fonts.googleapis.com/css2?family=Kalam:wght@300;400&family=Ruge+Boogie&display=swap">
<style>
  :root {
    --stage-plum: #5b1f52;
    --stage-dusk: #2f2229;
    --stage-ink: #0d0d0e;
    --cover-teal: #113b36;
    --cover-deep: #081614;
    --cover-black: #050606;
    --mist-violet: #8a3f8e;
    --mist-teal: #2f7a70;
    --potion-aqua: #7fd9c9;
    --potion-lilac: #b58fc6;
    --title-pink: #e0a9e6;
    --text-white: #f4f1f4;
    --logo-magenta: #b3127a;
  }
  * { box-sizing: border-box; margin: 0; padding: 0; }
  html, body { width: 1200px; height: 707px; overflow: hidden; }
  body {
    position: relative;
    background: linear-gradient(30deg, var(--stage-plum) 0%, var(--stage-dusk) 35%, #1c1a1c 65%, var(--stage-ink) 100%);
    font-family: "Kalam", "Segoe Script", cursive;
    color: var(--text-white);
  }
  .side-label {
    position: absolute;
    top: 78px;
    width: 456px;
    text-align: center;
    font-size: 32px;
    font-weight: 300;
    letter-spacing: 1px;
  }
  .side-label--front { left: 104px; }
  .side-label--back { left: 650px; }

  .cover {
    position: absolute;
    top: 150px;
    width: 456px;
    height: 456px;
    overflow: hidden;
  }
  .cover--front {
    left: 114px;
    background:
      radial-gradient(ellipse 70% 60% at 40% 45%, var(--cover-teal), var(--cover-deep) 60%, var(--cover-black) 100%);
  }
  .cover--back {
    left: 629px;
    background:
      radial-gradient(ellipse 55% 30% at 30% 10%, rgba(47,122,112,.55), transparent 75%),
      radial-gradient(ellipse 40% 35% at 30% 55%, rgba(120,140,140,.10), transparent 80%),
      linear-gradient(180deg, var(--cover-teal) 0%, var(--cover-deep) 45%, var(--cover-black) 100%);
  }

  .smoke-and-potion {
    position: absolute;
    inset: 0;
    background:
      radial-gradient(circle 78px at 51% 64%, var(--potion-aqua) 0%, #4f9c9a 45%, rgba(138,63,142,.75) 80%, transparent 100%),
      radial-gradient(ellipse 170px 90px at 62% 30%, rgba(138,63,142,.5), transparent 100%),
      radial-gradient(ellipse 190px 80px at 35% 12%, rgba(181,143,198,.28), transparent 100%);
  }

  .album-title {
    position: absolute;
    font-family: "Ruge Boogie", "Segoe Script", cursive;
    color: var(--title-pink);
    white-space: nowrap;
    text-shadow: 0 0 10px rgba(224,169,230,.45);
  }
  .album-title--front {
    left: 102px;
    top: 72px;
    font-size: 50px;
    transform: rotate(-6deg);
  }
  .album-title--back {
    left: 66px;
    top: 362px;
    font-size: 42px;
    transform: rotate(-4deg);
  }

  .artist-name {
    position: absolute;
    left: 342px;
    top: 366px;
    width: 100px;
    font-weight: 400;
    font-size: 18px;
    line-height: 22px;
    text-transform: uppercase;
    letter-spacing: 1px;
    color: var(--logo-magenta);
  }

  .track-list {
    position: absolute;
    left: 24px;
    top: 44px;
    width: 402px;
    list-style: none;
    font-size: 21px;
    font-weight: 300;
  }
  .track {
    display: flex;
    height: 44.6px;
    align-items: center;
  }
  .track__number { width: 46px; text-align: right; padding-right: 16px; }
  .track__name { flex: 1; }
  .track__time { width: 60px; text-align: right; }
</style>
</head>
<body>
  <h2 class="side-label side-label--front">Front</h2>
  <h2 class="side-label side-label--back">Back</h2>

  <section class="cover cover--front" aria-label="Front cover">
    <div class="smoke-and-potion" role="img" aria-label="Illustration of a glowing round potion flask with music notes, releasing violet and teal smoke"></div>
    <h1 class="album-title album-title--front">Lantern of Drift</h1>
    <p class="artist-name">Velvet<br>Circuitry</p>
  </section>

  <section class="cover cover--back" aria-label="Back cover">
    <ol class="track-list">
      <li class="track"><span class="track__number">1.</span><span class="track__name">Meadow Vs Ironclad</span><span class="track__time">6:54</span></li>
      <li class="track"><span class="track__number">2.</span><span class="track__name">Lantern of Drift</span><span class="track__time">6:10</span></li>
      <li class="track"><span class="track__number">3.</span><span class="track__name">Z O Lively</span><span class="track__time">8:04</span></li>
      <li class="track"><span class="track__number">4.</span><span class="track__name">Ever Roamin</span><span class="track__time">7:04</span></li>
      <li class="track"><span class="track__number">5.</span><span class="track__name">Bound to wander</span><span class="track__time">7:15</span></li>
      <li class="track"><span class="track__number">6.</span><span class="track__name">Fold into</span><span class="track__time">5:40</span></li>
      <li class="track"><span class="track__number">7.</span><span class="track__name">Past the Lanterns gate</span><span class="track__time">6:38</span></li>
    </ol>
    <p class="album-title album-title--back">Lantern of Drift</p>
    <p class="artist-name">Velvet<br>Circuitry</p>
  </section>
</body>
</html>
```